Business card design for QuelMarvion

I need a business card based on the logo design produced for QuelMarvion. The company is focused on triathlon and endurance sport coaching and the tag line is (per the logo) "Endurance. Resilience. Achievement". The design should be sophisticated, appropriate to an affluent and business oriented target market. Colors are optional but the color of the logo probably dictates the color used on the card. I envisage using the red logo, with black print for the wording and contact numbers on a white or cream background, but am open to alternative suggestions. I expect to select something fairly conventional, but would like to see some designs that are less conventional to stretch my thinking on what could be appropriate. I am assuming a single side design is best, but willing to consider double sided as an option.

Target Market(s)

Individual athletes and corporate health and wellness leaders

Industry/Entity Type

Health And Wellness

Contact Information for Business Card

The card should provide the following information:
Logo
My name: Gordon Lashby
Company website: QuelMarvion.com
My email: gordon.lashby@quelmarvion.com
My cell phone number: +1-555-018-2739

Font styles to use
Sans Serif

Colors

Designer to choose colors to be used in the design.

Requirements
Must have
• Space on the card - simple design, not over crowded.
Nice to have
• clean and clear font, nothing garish or mass market like
Should not have
• Do not add pictures

```html
<!DOCTYPE html>
<html lang="en">
<head>
<meta charset="UTF-8">
<title>QuelMarvion Business Card</title>
<link rel="stylesheet" href="https://fonts.googleapis.com/css2?family=Lato:wght@400;700&display=swap">
<style>
  :root {
    --page-bg: #e9e7e4;
    --brand-red: #ad2327;
    --brand-black: #0b0b0b;
    --ink-white: #ffffff;
    --badge-light: #f7f7f7;
    --badge-shade: #cfd0d2;
  }
  * { margin: 0; padding: 0; box-sizing: border-box; }
  html, body {
    width: 1200px;
    height: 900px;
    overflow: hidden;
    background: var(--page-bg);
    font-family: "Lato", sans-serif;
  }
  .business-card {
    position: absolute;
    left: 112px;
    top: 147px;
    width: 975px;
    height: 606px;
    border-radius: 22px;
    overflow: hidden;
    background: var(--brand-red);
    box-shadow: 0 10px 30px rgba(0,0,0,0.18);
  }
  .accent-band {
    position: absolute;
    left: 684px;
    top: 0;
    width: 291px;
    height: 100%;
    background: var(--brand-black);
  }
  .holder-name {
    position: absolute;
    left: 42px;
    top: 64px;
    color: var(--ink-white);
    font-size: 33px;
    font-weight: 400;
    letter-spacing: 0.5px;
    text-transform: uppercase;
  }
  .brand-badge {
    position: absolute;
    left: 438px;
    top: 50px;
    width: 510px;
    height: 510px;
    border-radius: 50%;
    background: radial-gradient(circle at 45% 40%, var(--badge-light) 0%, #ececed 45%, var(--badge-shade) 100%);
    display: flex;
    align-items: center;
    justify-content: center;
  }
  .brand-name {
    color: var(--brand-red);
    font-size: 66px;
    font-weight: 700;
    line-height: 1;
  }
  .contact-list {
    position: absolute;
    left: 42px;
    top: 444px;
    list-style: none;
    color: var(--ink-white);
    font-size: 25px;
    line-height: 36px;
  }
  .contact-item {
    display: flex;
    align-items: center;
  }
  .contact-icon {
    width: 20px;
    height: 20px;
    margin-right: 10px;
    flex: none;
  }
</style>
</head>
<body>
  <div class="business-card">
    <div class="accent-band"></div>
    <div class="holder-name">Gordon Lashby</div>
    <div class="brand-badge">
      <div class="brand-name">QuelMarvion</div>
    </div>
    <ul class="contact-list">
      <li class="contact-item">
        <svg class="contact-icon" viewBox="0 0 20 20" aria-hidden="true">
          <rect x="5" y="1.5" width="10" height="17" rx="2" fill="none" stroke="#fff" stroke-width="2"/>
          <rect x="6.5" y="4" width="7" height="9" fill="#fff"/>
          <circle cx="10" cy="15.7" r="1.1" fill="#fff"/>
        </svg>
        <span>+1-555-018-2739</span>
      </li>
      <li class="contact-item">
        <svg class="contact-icon" viewBox="0 0 20 20" aria-hidden="true">
          <circle cx="10" cy="10" r="8.5" fill="#fff"/>
          <path d="M6 5 q3 1 2 4 q-2 1 -1 4 q2 1 1 4 M13 4 q-1 3 2 4 q2 0 2 3" fill="none" stroke="#ad2327" stroke-width="1.6"/>
        </svg>
        <span>www.QuelMarvion.com</span>
      </li>
      <li class="contact-item">
        <svg class="contact-icon" viewBox="0 0 20 20" aria-hidden="true">
          <rect x="1.5" y="4" width="17" height="12" fill="#fff"/>
          <path d="M1.5 4 L10 11 L18.5 4" fill="none" stroke="#ad2327" stroke-width="1.5"/>
        </svg>
        <span>gordon.lashby@quelmarvion.com</span>
      </li>
    </ul>
  </div>
</body>
</html>
```